Meadowlyn Acres Website Design

We have been redeveloping our website already and are quite happy with the content, but the design needs to be better:
https://harvo-link.example-host.com/

Pages, content, concept etc. Can all be taken from the redeveloped website.
The farmer can register and edit/view their profile, subscribe and these pages need to be designed better as well as contact, about, pricing, tos, privacy and a page with example portlets.

We need a website to appeal to farmers, investors and retiring farmers.

The design should be clean and a little country.

We don't want any repeat designs that some may submit to every project and has no respect for the project brief, so please don't submit them.

Target Market(s)

farmers, investors, retirees

Industry/Entity Type

Farming

Number of Pages Required

5+ page

Colors

Designer to choose colors to be used in the design.

Requirements
Must have
• Nice, clean modern design that is appealing
• Profile page laid out nicely

```html
<!DOCTYPE html>
<html lang="en">
<head>
<meta charset="utf-8">
<title>Meadowlyn Acres</title>
<link rel="stylesheet" href="https://fonts.googleapis.com/css2?family=Arimo:wght@400;600;700&family=Cormorant+Garamond:ital,wght@1,500&family=Josefin+Sans:wght@300;400&display=swap">
<style>
:root{
  --ink:#2b2b2b;
  --brown:#3a2a14;
  --green:#2f7d2b;
  --logo-green:#5aa83a;
  --nav-active:#d9b24a;
  --rule:#d8d8d8;
  --grey-text:#9a9a9a;
  --salmon:#ef7e6a;
  --footer-top:#3e5d70;
  --footer-bottom:#5f7f90;
  --white:#ffffff;
}
*{margin:0;padding:0;box-sizing:border-box}
html,body{width:1200px;height:2903px;overflow:hidden;background:var(--white)}
body{position:relative;font-family:"Arimo",Arial,sans-serif;color:var(--ink)}
.abs{position:absolute}

/* header */
.site-header{left:8px;top:0;width:1184px;height:184px;border-left:1px solid var(--rule);border-right:1px solid var(--rule)}
.brand{left:470px;top:40px;display:flex;align-items:center;gap:14px}
.brand-dot{width:40px;height:40px;border-radius:50%;background:var(--logo-green)}
.brand-name{font-family:"Arimo",sans-serif;font-weight:600;font-size:21px;color:var(--ink)}
.main-nav{left:0;top:139px;width:1184px;height:36px}
.nav-item{position:absolute;top:9px;font-size:12px;color:#555;transform:translateX(-50%);white-space:nowrap}
.nav-item.is-active{color:var(--nav-active)}
.nav-divider{position:absolute;top:0;width:1px;height:34px;background:var(--rule)}

/* hero */
.hero-photo{top:184px;height:277px}
.hero-caption{left:72px;top:340px;color:var(--white);font-size:46px;line-height:48px;letter-spacing:-0.5px}

/* intro */
.intro{left:240px;top:480px;width:724px}
.intro-title{font-size:46px;font-weight:400;color:var(--brown);line-height:56px}
.intro-rule{height:1px;background:#8a7a5a;margin-top:2px}
.intro-text{font-size:10.5px;line-height:14px;margin-top:12px;color:#222}
.intro-text a{color:var(--brown)}
.btn-read{display:inline-block;margin-top:13px;background:var(--green);color:var(--white);font-size:12px;font-weight:600;width:96px;height:27px;line-height:27px;text-align:center}

/* aspiring farmers */
.steps-band{left:0;top:652px;width:1200px;height:496px;background:linear-gradient(180deg,#d9d6cf 0%,#c7c3b6 30%,#7c8064 55%,#5f7a3c 75%,#6d8a3a 100%)}
.steps-title{left:0;top:700px;width:1200px;text-align:center;font-family:"Cormorant Garamond",serif;font-style:italic;font-weight:500;font-size:68px;letter-spacing:3px;color:#2a2a2a}
.step-card{top:813px;height:302px;background:rgba(255,255,255,0.22);color:var(--white);text-align:center;font-family:"Josefin Sans",sans-serif;font-weight:300}
.step-label{margin-top:56px;font-family:"Cormorant Garamond",serif;font-style:italic;font-size:22px;letter-spacing:2px}
.step-number{font-family:"Cormorant Garamond",serif;font-style:italic;font-size:80px;line-height:76px}
.step-rule{width:44px;height:2px;background:var(--white);margin:16px auto 0}
.step-text{margin-top:30px;font-size:21px;line-height:28px;letter-spacing:1px}

/* video */
.video-panel{left:0;top:1157px;width:1188px;height:503px;background:linear-gradient(100deg,#5a2e26 0%,#8a3b33 22%,#2e3b55 40%,#3f6f9e 62%,#5d8fbf 80%,#3a4a55 100%)}
.video-title{left:0;top:1362px;width:1188px;text-align:center;color:var(--white);font-size:31px;letter-spacing:-0.5px}
.video-play{left:540px;top:1422px;display:flex;align-items:center;gap:8px;color:var(--white);font-size:15px;text-decoration:underline}

/* subscribe */
.subscribe-band{left:0;top:1660px;width:1200px;height:507px;background:linear-gradient(180deg,#7aa0d0 0%,#a9c3e4 35%,#5b7a3c 55%,#b9cde8 75%,#e6eef8 100%)}
.subscribe-card{left:244px;top:1680px;width:712px;height:391px;background:var(--white);text-align:center;font-family:"Josefin Sans",sans-serif;font-weight:300}
.subscribe-title{margin-top:26px;font-size:33px;line-height:39px;color:#444}
.benefits{list-style:none;margin-top:30px;font-size:17px;line-height:34.5px;color:var(--grey-text)}
.join-link{display:block;margin-top:26px;font-size:11px;color:#777;letter-spacing:0.5px}

/* testimonials */
.testimonials{left:0;top:2167px;width:1200px;height:662px;background:linear-gradient(180deg,#fafafa 0%,#f1f1f1 60%,#f7f7f7 100%)}
.testimonials-title{left:0;top:2208px;width:1200px;text-align:center;font-size:33px;color:#222}
.testimonial{top:2323px;width:240px;text-align:center}
.avatar{width:155px;height:155px;border-radius:50%;margin:0 auto;background:radial-gradient(circle at 50% 40%,#cfcfcf 0%,#a8a8a8 60%,#8c8c8c 100%)}
.t-name{margin-top:40px;font-family:"Josefin Sans",sans-serif;font-size:19px;color:var(--salmon)}
.t-text{margin:16px auto 0;width:196px;font-family:"Josefin Sans",sans-serif;font-weight:300;font-size:11px;line-height:16px;color:#666}
.t-quote{margin-top:36px;font-family:"Cormorant Garamond",serif;font-size:60px;line-height:40px;color:var(--salmon);font-weight:700}

/* footer */
.site-footer{left:0;top:2829px;width:1200px;height:74px;background:linear-gradient(180deg,var(--footer-top),var(--footer-bottom))}
.footer-text{left:226px;top:2862px;color:var(--white);font-size:11px;line-height:15px}
.footer-text a{color:var(--white)}
.social{left:918px;top:2862px;display:flex;gap:10px}
.social-dot{width:14px;height:14px;border-radius:50%;background:var(--white)}
</style>
</head>
<body>

<header class="abs site-header">
  <div class="abs brand">
    <span class="brand-dot"></span>
    <span class="brand-name">Meadowlyn Acres</span>
  </div>
  <nav class="abs main-nav">
    <span class="nav-item is-active" style="left:85px">Home</span>
    <span class="nav-divider" style="left:176px"></span>
    <span class="nav-item" style="left:292px">Aspiring Farmers</span>
    <span class="nav-divider" style="left:412px"></span>
    <span class="nav-item" style="left:509px">Investors</span>
    <span class="nav-divider" style="left:603px"></span>
    <span class="nav-item" style="left:718px">Retiring Farmer</span>
    <span class="nav-divider" style="left:832px"></span>
    <span class="nav-item" style="left:917px">Blog</span>
    <span class="nav-divider" style="left:998px"></span>
    <span class="nav-item" style="left:1091px">Contact</span>
  </nav>
</header>

<section class="hero">
  <div class="abs hero-photo" style="left:8px;width:29px;background:linear-gradient(180deg,#a9b2b8,#6b6a5e)" role="img" aria-label="Edge of a farm photo"></div>
  <div class="abs hero-photo" style="left:43px;width:365px;background:linear-gradient(180deg,#8d8f88 0%,#6a6a60 50%,#4f4a3a 100%)" role="img" aria-label="Open-sided farm shed on a grey day"></div>
  <div class="abs hero-photo" style="left:414px;width:370px;background:linear-gradient(180deg,#3f6fc6 0%,#8fb0e0 40%,#7a5a3c 62%,#4d7a2c 100%)" role="img" aria-label="Red barns and a fence under a blue sky"></div>
  <div class="abs hero-photo" style="left:790px;width:365px;background:linear-gradient(180deg,#8a8f92 0%,#9d6a5c 45%,#5c4a40 75%,#6a7a4a 100%)" role="img" aria-label="Farming father with two children and a dog"></div>
  <div class="abs hero-photo" style="left:1161px;width:31px;background:linear-gradient(180deg,#8a8a80,#5a5a48)" role="img" aria-label="Edge of a farm photo"></div>
  <div class="abs hero-caption">Your farm dream<br>can be a reality.</div>
</section>

<section class="abs intro">
  <h1 class="intro-title">You Can Own A Farm</h1>
  <div class="intro-rule"></div>
  <p class="intro-text">We know how hard it is for a young family to find the capital required to own and operate their own farm - so we started <a href="#">Meadowlyn Acres.</a><br>We want to rejuvenate regional Australia by putting farming back up the top of the career list for anyone.</p>
  <a class="btn-read">Read More</a>
</section>

<section>
  <div class="abs steps-band" role="img" aria-label="Sunlit paddock with hills and a horse rider"></div>
  <h2 class="abs steps-title">Aspiring Farmers</h2>
  <div class="abs step-card" style="left:219px;width:247px">
    <div class="step-label">Step</div>
    <div class="step-number">01</div>
    <div class="step-rule"></div>
    <div class="step-text">Register<br>as an Aspiring Farmer</div>
  </div>
  <div class="abs step-card" style="left:478px;width:246px">
    <div class="step-label">Step</div>
    <div class="step-number">02</div>
    <div class="step-rule"></div>
    <div class="step-text">Build your farm skills<br>to get yourself<br>farm-ready</div>
  </div>
  <div class="abs step-card" style="left:735px;width:248px">
    <div class="step-label">Step</div>
    <div class="step-number">03</div>
    <div class="step-rule"></div>
    <div class="step-text">together we find you<br>your dream farm</div>
  </div>
</section>

<section>
  <div class="abs video-panel" role="img" aria-label="Video still of a presenter standing beside a tractor"></div>
  <div class="abs video-title">Tom Hadley from Meadowlyn Acres</div>
  <div class="abs video-play">
    <svg width="30" height="30" viewBox="0 0 30 30"><circle cx="15" cy="15" r="13" fill="none" stroke="#fff" stroke-width="2"/><path d="M12 9 L21 15 L12 21 Z" fill="#fff"/></svg>
    <span>Play Video</span>
  </div>
</section>

<section>
  <div class="abs subscribe-band" role="img" aria-label="Rows of vines beneath a blue sky"></div>
  <div class="abs subscribe-card">
    <h2 class="subscribe-title" style="font-weight:300">Subscribe to be Either an Aspiring or<br>Premium Farmer to Receive:</h2>
    <ul class="benefits">
      <li>Free Fieldmark market analysis membership (valued at $300 pa)</li>
      <li>Farm business webinars (valued at $200)</li>
      <li>Corporate Partner Opportunities</li>
      <li>Public or Private profile (as required)</li>
      <li>Eligible to enter competitions and win prizes</li>
    </ul>
    <a class="join-link">JOIN NOW</a>
  </div>
</section>

<section>
  <div class="abs testimonials" role="img" aria-label="Soft, faded bright living room"></div>
  <h2 class="abs testimonials-title" style="font-weight:400">Testimonials</h2>
  <div class="abs testimonial" style="left:79px">
    <div class="avatar" role="img" aria-label="Portrait of a customer"></div>
    <div class="t-name">Name, Title</div>
    <p class="t-text">Land access is a major barrier to growing more farmers, and we are really excited to see the development of things like Meadowlyn Acres - creative ways to assist young or emerging farmers onto land!</p>
    <div class="t-quote">”</div>
  </div>
  <div class="abs testimonial" style="left:484px">
    <div class="avatar" role="img" aria-label="Portrait of a customer"></div>
    <div class="t-name">Name, Title</div>
    <p class="t-text">Meadowlyn Acres can offer an opportunity to put people with the skills and ambition, with either a farming family looking to transition into retirement or for someone who doesn't have the skills but has capital and wants somewhere safe to invest.</p>
    <div class="t-quote">”</div>
  </div>
  <div class="abs testimonial" style="left:884px">
    <div class="avatar" role="img" aria-label="Portrait of a customer"></div>
    <div class="t-name">Name, Title</div>
    <p class="t-text">We both like the idea that Meadowlyn Acres could have the ability to get more young people into small rural areas. We both love rural Australia and think it's a shame so many areas are dying, as less young people take on family farms.</p>
    <div class="t-quote">”</div>
  </div>
</section>

<footer class="abs site-footer"></footer>
<div class="abs footer-text"><a href="#">Meadowlyn Acres</a><br>© Meadowlyn Acres 2017</div>
<div class="abs social">
  <span class="social-dot"></span><span class="social-dot"></span><span class="social-dot"></span>
</div>

</body>
</html>
```